Maple Syrup Bottle (front) Label design

I need label design for a 16fl OZ rectangular bottle of maple syrup with the usable dimensions of: Front: 4" x 2" and the back area for "ingredient specifications" of: 6" x 2". The maple syrup product comes from our own farm and is a quality product. The technical name/class of the syrup is: Grade A / AMBER
Updates

I can’t seem to find a way to upload a photo of the maple syrup bottle, but the front dimensions are clearly written on bottle description. Again: 4.5” by 2.25”

I have tried to upload the photo of the maple syrup bottle several times, and it seems (from my side) that it is successful. But I can never find it and the artists cannot find it either. Not sure what to do.

I have tried several times to add a photo of maple bottle, but it never shows up

This seems to be a futile exercise

I would like to post some images of the actual quill Hollow (not the one on Fendix, though!
But I can’t get back to the page that allows that to happen. Please advise!

Somebody PLEASE ask PW management to make it possible for me to upload more images! The "add photos" etc. just disappears from anywhere.

Target Market(s)

High-end food stores

Industry/Entity Type

Maple syrup retail industry

Other font styles liked:
• I don't know, and welcome suggestions

Colors

Designer to choose colors to be used in the design.

Requirements
Must have
• Name of Farm: Quill Hollow Maple
Nice to have
• The label can be "minimalist" and elegant. There is already a Maple leaf glass relief on the top of front of the bottle.
Should not have
• and NOT include farm buildings with steam coming out the chimney, etc.

```html
<!DOCTYPE html>
<html lang="en">
<head>
<meta charset="utf-8">
<title>Quill Hollow Maple – Maple Syrup Front Label</title>
<link rel="stylesheet" href="https://fonts.googleapis.com/css2?family=Montserrat:wght@800&family=Open+Sans:wght@300;400&display=swap">
<style>
  :root {
    --bg: #e3e3e3;
    --label: #ffffff;
    --orange: #f07a1f;
    --orange-deep: #c8561a;
    --charcoal: #58595b;
    --ink: #3b3b3b;
  }
  html, body {
    margin: 0;
    padding: 0;
    width: 1200px;
    height: 1200px;
    overflow: hidden;
    background: var(--bg);
  }
  .canvas {
    position: relative;
    width: 1200px;
    height: 1200px;
  }
  .label-shape {
    position: absolute;
    left: 0;
    top: 0;
  }
  .label-text {
    position: absolute;
    left: 330px;
    width: 540px;
    text-align: center;
    margin: 0;
  }
  .farm-name {
    top: 282px;
    font-family: "Montserrat", sans-serif;
    font-weight: 800;
    font-size: 29px;
    line-height: 1;
    letter-spacing: 0.5px;
    color: var(--charcoal);
  }
  .product-name {
    top: 718px;
    font-family: "Montserrat", sans-serif;
    font-weight: 800;
    font-size: 88px;
    line-height: 78px;
    letter-spacing: -1px;
  }
  .product-name .word-maple { color: var(--orange); display: block; }
  .product-name .word-syrup { color: var(--charcoal); display: block; }
  .grade {
    top: 898px;
    font-family: "Open Sans", sans-serif;
    font-weight: 300;
    font-size: 35px;
    line-height: 1;
    letter-spacing: -0.5px;
    color: var(--ink);
  }
  .purity {
    top: 956px;
    font-family: "Open Sans", sans-serif;
    font-weight: 400;
    font-size: 21px;
    line-height: 1;
    color: #ffffff;
  }
  .volume {
    top: 1040px;
    font-family: "Open Sans", sans-serif;
    font-weight: 400;
    font-size: 25px;
    line-height: 1;
    color: var(--charcoal);
  }
  .volume .paren { color: var(--orange); }
</style>
</head>
<body>
<main class="canvas">
  <svg class="label-shape" width="1200" height="1200" viewBox="0 0 1200 1200" aria-hidden="true">
    <defs>
      <linearGradient id="rim" x1="0" y1="0" x2="1" y2="1">
        <stop offset="0" stop-color="#f39a2a"/>
        <stop offset="1" stop-color="#c8561a"/>
      </linearGradient>
    </defs>
    <!-- label body -->
    <rect class="label-body" x="330" y="50" width="540" height="1100" rx="270" ry="270" fill="var(--label)"/>
    <rect class="label-rim" x="344" y="64" width="512" height="1072" rx="256" ry="256" fill="none" stroke="url(#rim)" stroke-width="2"/>

    <!-- farm mark: plain circle -->
    <circle class="farm-mark" cx="600" cy="180" r="95" fill="var(--charcoal)"/>

    <!-- rule under farm name with drip bowl -->
    <line class="farm-rule" x1="482" y1="328" x2="718" y2="328" stroke="var(--orange)" stroke-width="3"/>
    <path class="drip-bowl" d="M505 330 Q600 385 695 330 Z" fill="var(--charcoal)"/>

    <!-- syrup drip -->
    <path class="syrup-drip" fill="var(--orange)"
      d="M576 352 C590 358 597 372 597 398 L597 606 C597 626 575 640 575 664 A25 25 0 0 0 625 664 C625 640 603 626 603 606 L603 398 C603 372 610 358 624 352 Z"/>

    <!-- rules around grade -->
    <line class="grade-rule" x1="455" y1="889" x2="745" y2="889" stroke="var(--orange)" stroke-width="2"/>
    <line class="grade-rule" x1="455" y1="950" x2="745" y2="950" stroke="var(--orange)" stroke-width="2"/>

    <!-- purity tab -->
    <path class="purity-tab" d="M514 950 L686 950 L676 972 Q672 982 660 982 L540 982 Q528 982 524 972 Z" fill="var(--orange)"/>
  </svg>

  <p class="label-text farm-name">QUILL HOLLOW MAPLE FARM</p>
  <h1 class="label-text product-name"><span class="word-maple">MAPLE</span><span class="word-syrup">SYRUP</span></h1>
  <p class="label-text grade">GRADE A / AMBER</p>
  <p class="label-text purity">100% PURE</p>
  <p class="label-text volume">16fl OZ <span class="paren">(</span> 473 ml <span class="paren">)</span></p>
</main>
</body>
</html>
```